Background of Our Business: PRJ Financial Services provides accounting and tax services to small businesses. Website: www.prjfs-example.com.au. Our slogan is: one stop finance department service for small businesses.
I would like a flyer design with 2 sides.
1st side)
Business Logo; PRJ - Finance Department Service for Small Businesses (Please refer file 1 as attached)

Large text of: Too many things going on? Smaller text: Let us reduce your input into accounts, you can focus on more value adding areas.

Our Services: Bookkeeping, Payroll, Financial Statement, Tax Advisory, Tax Return, Business Performance Measurement, Business Decision Support, Assistance in Loan Applications, and much more.

Why Us: Our clients are handpicked, we are fully committed to your business, and our works are performed at corporate standard. We utilise technology to save your accounting cost, monitor your compliance risks, provide solid data for business decision making, and be your representative in dealing with banks and UDQ. (Please also refer file 2 as attached)

Contact details: Address: 17 Moreton Lane, Carlisle, WA 6101
PO Box 2394, East Victoria Park, WA 6981
Tel: (08) 5550 2291; Mob: 0400 555 219

2nd side)
Our Pricing: Charge by transaction volumes; Fixed fee advised beforehand. hourly rate please refer file 4 as attached.

Our 'Gold' level service subscriber receives:
Frequent bookkeeping, payroll, and financial reporting services
Integrate tax advisory, compliance risk monitoring and control
Free regular preliminary business performance check
Free assistance in commercial loan and mortgage application
Free hand picked business insights for your industry
Free representative service for you in dealing with banks, UDQ.

Coupon Section: Sign up now and receive 10% off for your next 12 months bill. Valid until 31/07/2016.

```html
<!DOCTYPE html>
<html lang="en">
<head>
<meta charset="utf-8">
<title>PRJ Financial Services – Flyer</title>
<link rel="stylesheet" href="https://fonts.googleapis.com/css2?family=Oswald:wght@500;700&family=Open+Sans:wght@400;600;700&display=swap">
<style>
:root{
  --backdrop:#7a4f2c;
  --navy:#173f78;
  --navy-deep:#123464;
  --ink:#2b2b2b;
  --muted:#444;
  --mist:#c9d6da;
  --paper:#ffffff;
  --pale:#eef0f2;
  --tier-grey:#8c8f92;
  --tier-body:#cfcfcf;
  --gold-head:#12707f;
  --gold-body:#22b5d3;
}
*{box-sizing:border-box;margin:0;padding:0}
html,body{width:1200px;height:804px;overflow:hidden}
body{background:var(--backdrop);font-family:"Open Sans",Arial,sans-serif;color:var(--ink);position:relative}
.sheet{position:absolute;background:var(--paper);box-shadow:2px 3px 6px rgba(0,0,0,.35);overflow:hidden}
.sheet--front{left:74px;top:70px;width:516px;height:664px}
.sheet--back{left:610px;top:71px;width:517px;height:666px}
.abs{position:absolute}
.condensed{font-family:"Oswald","Arial Narrow",sans-serif;font-weight:700}

/* front */
.hero-photo{left:0;top:0;width:516px;height:360px;background:linear-gradient(160deg,#6f9fca 0%,#b9d3ea 35%,#e8eef4 65%,#9fb2c4 100%)}
.hero-fade{left:0;top:300px;width:516px;height:70px;background:linear-gradient(180deg,rgba(255,255,255,0),#fff)}
.headline{left:30px;top:22px;width:150px;text-align:center;color:#fff;font-size:29px;line-height:36px;text-shadow:1px 2px 3px rgba(0,0,0,.5);text-transform:uppercase}
.brand{left:266px;top:22px;width:232px}
.brand__name{display:flex;align-items:center;gap:10px;font-family:"Open Sans",sans-serif;font-weight:700;color:var(--navy);font-size:52px;line-height:60px}
.brand__dot{width:34px;height:34px;border-radius:50%;background:var(--navy)}
.brand__rule{height:1px;background:var(--navy);margin-top:6px}
.brand__tag{font-size:9.5px;color:var(--navy);margin-top:5px;white-space:nowrap}
.url-tab{left:16px;top:322px;width:266px;height:34px;background:var(--navy-deep);border-radius:0 34px 0 0;color:#fff;font-weight:700;font-size:16px;letter-spacing:.5px;line-height:34px;padding-left:32px}
.section-title{font-size:14px;font-weight:600;color:var(--navy)}
.services{left:21px;top:363px}
.bullets{list-style:none;margin-top:7px}
.bullets li{position:relative;padding-left:12px;font-size:8px;line-height:10.6px;color:var(--muted)}
.bullets li::before{content:"";position:absolute;left:0;top:3px;width:6px;height:6px;border-radius:50%;background:var(--navy)}
.paper-stack{left:168px;top:363px;width:64px;height:156px;background:linear-gradient(180deg,#f4f4f4,#d9dcdf)}
.why{left:21px;top:505px;width:214px}
.why p{margin-top:6px;font-size:7.4px;line-height:11.6px;text-align:justify;color:var(--muted)}
.pitch-box{left:252px;top:376px;width:241px;height:209px;background:var(--mist)}
.pitch-box__text{margin:9px 10px 0;text-align:center;font-family:"Oswald",sans-serif;font-weight:500;font-size:17px;line-height:23px;color:#3a3a3a}
.contact{left:266px;top:468px;width:213px;height:99px;background:var(--navy);border:2px solid #fff;border-radius:8px;box-shadow:0 0 0 1px var(--navy);color:#fff;padding:2px 10px}
.contact__line{font-family:"Oswald",sans-serif;font-weight:700;font-size:17px;line-height:25px;border-bottom:1px solid rgba(255,255,255,.6)}
.contact__addr{font-size:9px;line-height:14.5px;margin-top:4px}
.slogan{color:var(--navy);font-size:24px;line-height:27px;text-transform:uppercase;letter-spacing:.2px}
.slogan--front{left:22px;top:598px}
.mini-brand{width:140px}
.mini-brand__name{display:flex;align-items:center;gap:6px;font-weight:700;color:var(--navy);font-size:32px;line-height:38px}
.mini-brand__dot{width:20px;height:20px;border-radius:50%;background:var(--navy)}
.mini-brand__tag{font-size:5.6px;color:var(--navy);white-space:nowrap;margin-top:2px}
.mini-brand--front{left:354px;top:598px}

/* back */
.top-band{left:0;top:0;width:517px;height:47px;background:var(--navy)}
.top-band h2{position:absolute;top:18px;color:#fff;font-size:14px;font-weight:600}
.info-band{left:0;top:47px;width:517px;height:80px;background:var(--pale)}
.info-list{position:absolute;top:4px;list-style:none}
.info-list li{position:relative;padding-left:12px;font-size:7.4px;line-height:11.6px;color:var(--muted)}
.info-list li::before{content:"";position:absolute;left:0;top:3px;width:6px;height:6px;border-radius:50%;background:var(--navy)}
.price-table{left:19px;top:143px;width:476px;height:191px;background:#fff;box-shadow:0 0 4px rgba(0,0,0,.3)}
.tier{position:absolute;top:12px;width:150px;height:167px}
.tier__head{height:32px;background:var(--tier-grey);color:#fff;font-family:"Oswald",sans-serif;font-weight:700;font-size:15px;line-height:32px;padding-left:7px}
.tier__head small{font-size:11px}
.tier__body{height:135px;background:var(--tier-body);padding:10px 9px 0}
.tier__rates{list-style:none;font-size:7px;font-weight:700;line-height:13.2px;color:#222}
.tier__note{margin-top:11px;padding-top:7px;border-top:1px solid rgba(255,255,255,.7);font-size:6.6px;line-height:10.5px;color:#333}
.tier--gold .tier__head{background:var(--gold-head)}
.tier--gold .tier__body{background:var(--gold-body)}
.tier--gold .tier__rates,.tier--gold .tier__note{color:#0f2a44}
.coupon{left:0;top:349px;width:517px;height:194px;background:var(--navy);color:#fff}
.coupon__title{position:absolute;left:38px;top:14px;font-size:26px;line-height:32px}
.coupon__offer{position:absolute;left:38px;top:52px;width:200px;font-size:21.5px;line-height:26.5px}
.coupon-photo{left:246px;top:358px;width:238px;height:177px;background:linear-gradient(135deg,#e9eef3 0%,#b7c3cf 50%,#39424c 100%)}
.url-band{left:0;top:543px;width:517px;height:42px;background:var(--mist)}
.url-band__url{position:absolute;left:30px;top:10px;font-weight:700;font-size:16px;color:#111}
.url-band__addr{position:absolute;left:262px;top:4px;font-size:12px;line-height:17px;color:#111}
.slogan--back{left:26px;top:597px}
.mini-brand--back{left:358px;top:597px}
</style>
</head>
<body>

<section class="sheet sheet--front" aria-label="Flyer front">
  <div class="abs hero-photo" role="img" aria-label="Photo of hands using a tablet with a pen, glasses and financial reports on a desk"></div>
  <div class="abs hero-fade"></div>
  <h1 class="abs headline condensed">Too many things going on?</h1>
  <div class="abs brand">
    <div class="brand__name"><span class="brand__dot"></span>PRJ</div>
    <div class="brand__rule"></div>
    <div class="brand__tag">Finance Department Service for Small Businesses</div>
  </div>
  <div class="abs url-tab">www.prjfs-example.com.au</div>

  <div class="abs paper-stack" role="img" aria-label="Photo of a tall stack of paper documents"></div>
  <div class="abs services">
    <h2 class="section-title">Our Services:</h2>
    <ul class="bullets">
      <li>Bookkeeping</li><li>Payroll</li><li>Tax Return</li><li>Financial Statement</li><li>Tax Advisory</li>
      <li>Business Performance</li><li>Measurement</li><li>Business Decision Support</li>
      <li>Assistance in Loan Applications</li><li>and much more</li>
    </ul>
  </div>
  <div class="abs why">
    <h2 class="section-title">Why Us:</h2>
    <p>Our clients are handpicked, we are fully committed to your business, and our works are performed at corporate standard. We utilise technology to save your accounting cost, monitor your compliance risks, provide solid data for business decision making, and be your representative in dealing with banks and UDQ.</p>
  </div>

  <div class="abs pitch-box">
    <p class="pitch-box__text">Let us reduce your input into accounts, you can focus on more value adding areas.</p>
  </div>
  <div class="abs contact">
    <div class="contact__line">Tel: (08) 5550 2291</div>
    <div class="contact__line">Mob: 0400 555 219</div>
    <div class="contact__addr">17 Moreton Lane, Carlisle, WA 6101<br>PO Box 2394, East Victoria Park, WA 6981</div>
  </div>

  <p class="abs slogan slogan--front condensed">One stop finance department<br>service for small businesses</p>
  <div class="abs mini-brand mini-brand--front">
    <div class="mini-brand__name"><span class="mini-brand__dot"></span>PRJ</div>
    <div class="mini-brand__tag">Finance Department Service for Small Businesses</div>
  </div>
</section>

<section class="sheet sheet--back" aria-label="Flyer back">
  <div class="abs top-band">
    <h2 style="left:35px">Our Pricing:</h2>
    <h2 style="left:190px">Our 'Gold' level service subscriber receives:</h2>
  </div>
  <div class="abs info-band">
    <ul class="info-list" style="left:35px;width:140px">
      <li>Charge by transaction volumes</li>
      <li>Fixed fee advised beforehand</li>
      <li>Hourly rate please refer file 4 as attached</li>
    </ul>
    <ul class="info-list" style="left:190px">
      <li>Frequent bookkeeping, payroll, and financial reporting services</li>
      <li>Integrate tax advisory, compliance risk monitoring and control</li>
      <li>Free regular preliminary business performance check</li>
      <li>Free assistance in commercial loan and mortgage application</li>
      <li>Free hand picked business insights for your industry</li>
      <li>Free representative service for you in dealing with banks, UDQ.</li>
    </ul>
  </div>

  <div class="abs price-table">
    <div class="tier" style="left:11px">
      <div class="tier__head">BRONZE</div>
      <div class="tier__body">
        <ul class="tier__rates">
          <li>Bookkeeping &amp; Payroll: &nbsp;$50/hr</li><li>Taxation: &nbsp;$110/hr</li>
          <li>Management Accounting: $110/hr</li><li>Finance: &nbsp;POA, Generally Free</li><li>General Consulting: &nbsp;Free*</li>
        </ul>
        <p class="tier__note">Rate above applies for using us for bookkeeping or payroll or taxation or management accounting servic</p>
      </div>
    </div>
    <div class="tier tier--gold" style="left:165px">
      <div class="tier__head">GOLD <small>(MOST POPULAR)</small></div>
      <div class="tier__body">
        <ul class="tier__rates">
          <li>Bookkeeping &amp; Payroll: &nbsp;$45/hr</li><li>Taxation: &nbsp;$99/hr</li>
          <li>Management Accounting: &nbsp;$99/hr</li><li>Finance: &nbsp;POA, Generally Free</li><li>General Consulting: &nbsp;Free*</li>
        </ul>
        <p class="tier__note">Rate above applies for using us for bookkeeping or payroll or management accounting and taxation services.</p>
      </div>
    </div>
    <div class="tier" style="left:320px">
      <div class="tier__head">PLATINUM</div>
      <div class="tier__body">
        <ul class="tier__rates">
          <li>Bookkeeping &amp; Payroll: 45/hr</li><li>Taxation:$99/hr</li>
          <li>Management Accounting:$99/hr</li><li>Finance POA, Generally Free</li><li>General Consulting: &nbsp;Free*</li>
        </ul>
        <p class="tier__note">Rate above applies for using us for bookkeeping or payroll or management accounting and taxation services.</p>
      </div>
    </div>
  </div>

  <div class="abs coupon">
    <h2 class="coupon__title condensed">COUPON SECTION:</h2>
    <p class="coupon__offer condensed">Sign up now and receive 10% off for your next 12 months bill. Valid until 31/07/2016.</p>
  </div>
  <div class="abs coupon-photo" role="img" aria-label="Photo of business people reviewing printed charts and graphs"></div>

  <div class="abs url-band">
    <span class="url-band__url">www.prjfs-example.com.au</span>
    <span class="url-band__addr">17 Moreton Lane, Carlisle, WA 6101<br>PO Box 2394, East Victoria Park, WA 6981</span>
  </div>

  <p class="abs slogan slogan--back condensed">One stop finance department<br>service for small businesses</p>
  <div class="abs mini-brand mini-brand--back">
    <div class="mini-brand__name"><span class="mini-brand__dot"></span>PRJ</div>
    <div class="mini-brand__tag">Finance Department Service for Small Businesses</div>
  </div>
</section>

</body>
</html>
```